Wedding Guestbook/Questionnaire Pages

I am looking for questionnaire-style guest book pages for a friend's wedding. The bride wants her guests to fill out a page of reflections on the couple and the wedding in lieu of a traditional guest book. The pages would be printed on 12x12 paper and bound in a book after the wedding.

I've attached a photo of the style of the pages as well as several documents that show colors and give a feel for the wedding.

I understand that this isn't a common project so I welcome any questions and would be more than happy to clarify things.

Thank you!

Target Market(s)

The bride and groom are a young couple and the wedding is more fun and whimisical than formal. The colors are primarily purple with green and silver accents.

Industry/Entity Type

Wedding

Requirements
Must have
• I would like to have 2 pages that are similar, but have different questions on them so that every guest doesn't answer the same questions. On each page it needs to say 'Mara & Declan,' 'May 27th, 2011,' and a place that says 'Guest Names' for the guest sign their names.
Nice to have
• Some of the questions we like are:
Do you have any advice or wishes for the bride and groom?
How far did you travel to get here?
How do you know Mara and Declan?
What’s your favorite memory with the bride and groom?
What has been your favorite part of the wedding?
What do you think they'll name their children?
Should not have
• The pages do not need to be extremely colorful. An ivory or white background with accents of color would be preferred.

```html
<!DOCTYPE html>
<html lang="en">
<head>
<meta charset="utf-8">
<title>Mara &amp; Declan — Guestbook Pages</title>
<link rel="stylesheet" href="https://fonts.googleapis.com/css2?family=Great+Vibes&family=Courgette&family=Arimo&display=swap">
<style>
  :root {
    --paper: #ffffff;
    --leaf: #6f9c22;
    --plum: #6b2a8f;
    --orchid: #8d2a9c;
    --lilac: #b99ae0;
    --ink: #1d1d1d;
    --fold: #c9c9c9;
  }
  * { margin: 0; padding: 0; box-sizing: border-box; }
  html, body { width: 1200px; height: 604px; overflow: hidden; background: var(--paper); }
  .spread { position: relative; width: 1200px; height: 604px; overflow: hidden; background: var(--paper); }
  .rules { position: absolute; inset: 0; width: 1200px; height: 604px; }
  .couple {
    position: absolute; font-family: "Great Vibes", cursive;
    color: var(--leaf); font-size: 38px; line-height: 1; white-space: nowrap;
  }
  .date {
    position: absolute; font-family: "Arimo", Arial, sans-serif;
    color: var(--plum); font-size: 21px; line-height: 1; white-space: nowrap;
  }
  .prompt {
    position: absolute; font-family: "Courgette", cursive;
    color: var(--ink); font-size: 16.5px; line-height: 1.3; white-space: nowrap;
  }
  .bouquet {
    position: absolute; left: 2px; top: 82px; width: 66px; height: 62px;
    border-radius: 50%; background: radial-gradient(circle at 45% 40%, #a540b4, var(--orchid) 55%, #6d1d7c);
  }
  .sparkle {
    position: absolute; width: 12px; height: 12px; border-radius: 50%;
    background: var(--lilac);
  }
</style>
</head>
<body>
<main class="spread">
  <svg class="rules" viewBox="0 0 1200 604" aria-hidden="true">
    <line x1="599" y1="0" x2="599" y2="604" stroke="var(--fold)" stroke-width="1" stroke-dasharray="2 3"/>
    <polyline points="25,604 25,61 343,61" fill="none" stroke="var(--leaf)" stroke-width="3.5"/>
    <polyline points="37,604 37,70 160,70" fill="none" stroke="var(--plum)" stroke-width="1.6"/>
    <g fill="none" stroke="var(--leaf)" stroke-width="1.8" stroke-dasharray="11 4 2 4">
      <line x1="969" y1="18" x2="969" y2="229"/>
      <line x1="810" y1="229" x2="1200" y2="229"/>
      <line x1="810" y1="229" x2="810" y2="525"/>
      <line x1="611" y1="300" x2="810" y2="300"/>
      <line x1="810" y1="525" x2="1177" y2="525"/>
      <line x1="1177" y1="229" x2="1177" y2="525"/>
    </g>
  </svg>

  <section class="page page-left">
    <p class="couple" style="left:347px; top:6px;">Mara&amp;Declan</p>
    <p class="date" style="left:162px; top:38px;">May 27th, 2011</p>
    <div class="bouquet" role="img" aria-label="Purple flower bouquet ornament"></div>
    <span class="sparkle" role="img" aria-label="Lilac sparkle" style="left:24px; top:166px;"></span>
    <span class="sparkle" role="img" aria-label="Lilac sparkle" style="left:34px; top:356px;"></span>
    <span class="sparkle" role="img" aria-label="Lilac sparkle" style="left:334px; top:344px;"></span>
    <p class="prompt guest-name" style="left:70px; top:88px;">Guest Name</p>
    <p class="prompt" style="left:53px; top:172px;">Do you have any advice or wishes for the bride and groom?</p>
    <p class="prompt" style="left:53px; top:366px;">How do you know<br>Mara and Declan?</p>
    <p class="prompt" style="left:330px; top:370px;">What has been your favorite<br>part of the wedding?</p>
  </section>

  <section class="page page-right">
    <p class="prompt" style="left:636px; top:28px;">What is your favorite memory with<br>the bride and groom?</p>
    <p class="prompt guest-name" style="left:1087px; top:28px;">guest name</p>
    <p class="prompt" style="left:958px; top:234px;">What do you think they'll<br>name their children? Why?</p>
    <p class="prompt" style="left:636px; top:308px;">How far did you<br>travel to get here?</p>
    <p class="date" style="left:812px; top:552px;">May 27th, 2011</p>
    <p class="couple" style="right:22px; top:536px;">Mara&amp;Declan</p>
  </section>
</main>
</body>
</html>
```